A book titled The Lantern Kept Her Quiet Map. It's intended to change peoples perspective of the streets

Title: The Lantern Kept Her Quiet Map
Subtitile: So They Keep On Hoping For Rain. (Doesn't really have to be on the cover, you decide.)
Author: Delmar Fitzwaterly
Book Size: 6x9 I need a book cover design for my first book. It's a very short book 60-70 pages. It is a book that points out the tricks the devil uses to get people to run the streets. It's meant to destroy some of the patterns that have been set in place in neighborhoods that are considered bad.
I didn't want to tell people what the book was about at all so that whoever came the closest to displaying what I was thinking would be the winner. Since I have given you a snippet of what it is about, I won't lead you any further. Whatever colors, whatever theme, whatever you come up with is totally up to you.

Target Market(s)

18-35 year olds

Requirements
Must have
• At this point I don't want to interfere with the creativity that could come forth. This might be a premature decision on my part. I don't want to say add this or I don't want this. I want it to be as special as I feel the title and the book is. I want it to be compelling enough, and coincide with the title enough that someone has to pick it up to read it.
Nice to have
• At this point I don't want to interfere with the creativity that could come forth. This might be a premature decision on my part. I don't want to say add this or I don't want this.
Should not have

```html
<!DOCTYPE html>
<html lang="en">
<head>
<meta charset="utf-8">
<title>The Lantern Kept Her Quiet Map — Cover Spread</title>
<link rel="stylesheet" href="https://fonts.googleapis.com/css2?family=Bebas+Neue&family=Bowlby+One&family=Old+Standard+TT&family=Playfair+Display:ital@1&display=swap">
<style>
  :root {
    --back-red: #b92600;
    --spine-black: #0c0807;
    --title-red: #b8260c;
    --title-white: #ffffff;
    --title-orange: #e2592b;
    --photo-light: #c7b9a4;
    --photo-mid: #4a3022;
    --photo-dark: #0b0706;
    --figure-orange: #c2502a;
  }
  * { margin: 0; padding: 0; box-sizing: border-box; }
  html, body { width: 1200px; height: 864px; overflow: hidden; background: var(--back-red); }
  .cover-spread { position: relative; width: 1200px; height: 864px; }

  .back-cover { position: absolute; left: 0; top: 0; width: 576px; height: 864px; background: var(--back-red); }

  .spine {
    position: absolute; left: 576px; top: 0; width: 48px; height: 864px;
    background: var(--spine-black);
    display: flex; flex-direction: column; align-items: center;
    padding-top: 40px;
  }
  .spine-title, .spine-author {
    writing-mode: vertical-rl;
    white-space: nowrap;
    line-height: 1;
  }
  .spine-title { font-family: "Bebas Neue", sans-serif; font-size: 42px; color: var(--title-white); }
  .spine-title .word-the, .spine-title .word-quiet {
    font-family: "Playfair Display", serif; font-style: italic; font-size: 26px; margin: 0 0 6px;
  }
  .spine-title .word-lantern { color: var(--title-red); }
  .spine-title .word-map { font-family: "Bowlby One", sans-serif; font-size: 28px; color: var(--title-orange); }
  .divider-dot {
    display: block; width: 10px; height: 10px; border-radius: 50%;
    background: var(--title-white);
  }
  .spine .divider-dot { margin: 50px 0 52px; }
  .spine-author { font-family: "Old Standard TT", serif; font-size: 20px; color: var(--title-white); }

  .front-cover { position: absolute; left: 624px; top: 0; width: 576px; height: 864px; overflow: hidden; }
  .cover-photo {
    position: absolute; inset: 0;
    background:
      radial-gradient(ellipse 150px 260px at 50% 72%, var(--figure-orange) 0%, rgba(194,80,42,0.35) 45%, rgba(0,0,0,0) 100%),
      linear-gradient(180deg, var(--photo-light) 0%, var(--photo-mid) 40%, var(--photo-dark) 72%, var(--photo-dark) 100%);
  }

  .front-title { position: absolute; left: 168px; top: 0; color: var(--title-white); line-height: 1; }
  .front-title span { position: absolute; left: 0; white-space: nowrap; }
  .front-title .word-the { top: 38px; font-family: "Playfair Display", serif; font-style: italic; font-size: 46px; }
  .front-title .word-lantern { top: 112px; font-family: "Bebas Neue", sans-serif; font-size: 104px; color: var(--title-red); }
  .front-title .word-kept { top: 208px; font-family: "Bebas Neue", sans-serif; font-size: 104px; }
  .front-title .word-her { top: 304px; font-family: "Bebas Neue", sans-serif; font-size: 104px; }
  .front-title .word-quiet { top: 650px; font-family: "Playfair Display", serif; font-style: italic; font-size: 40px; }
  .front-title .word-map { top: 696px; font-family: "Bowlby One", sans-serif; font-size: 58px; color: var(--title-orange); }

  .front-cover .divider-dot { position: absolute; left: 279px; top: 783px; }
  .front-author {
    position: absolute; left: 0; width: 568px; top: 812px; text-align: center;
    font-family: "Old Standard TT", serif; font-size: 24px; color: var(--title-white);
  }
</style>
</head>
<body>
<div class="cover-spread">
  <div class="back-cover"></div>

  <div class="spine">
    <div class="spine-title">
      <span class="word-the">the</span> <span class="word-lantern">LANTERN</span> KEPT HER <span class="word-quiet">quiet</span> <span class="word-map">MAP</span>
    </div>
    <span class="divider-dot" aria-hidden="true"></span>
    <div class="spine-author">Delmar Fitzwaterly</div>
  </div>

  <div class="front-cover">
    <div class="cover-photo" role="img" aria-label="Photograph of a dim hallway with a hooded figure in an orange sweatshirt sitting alone on the floor"></div>
    <h1 class="front-title">
      <span class="word-the">the</span>
      <span class="word-lantern">LANTERN</span>
      <span class="word-kept">KEPT</span>
      <span class="word-her">HER</span>
      <span class="word-quiet">quiet</span>
      <span class="word-map">MAP</span>
    </h1>
    <span class="divider-dot" aria-hidden="true"></span>
    <p class="front-author">Delmar Fitzwaterly</p>
  </div>
</div>
</body>
</html>
```